This will turn into a huge project with mass exposure.

Bright Harbor creates soap, perfumes, rubs, lotion, etc for some of the most know brands in the market: Juliana Charm, Soak & Skin Studio, PGL sports teams, etc.

They are going to be redesigning all logos, labels, websites and print.

They are starting with a business card and logo.

ALL designs must include a logo for Bright Harbor International

Reason: Need more design options

Target Market(s)

Purchasers such as Julana Charm

Industry/Entity Type

Business

Requirements
Must have
• a space for Qr code

two sided

Info:
Peter Malvo, President
info@brightharbor-example.com
555-014-7392
Nice to have
• Colors: gray background with blue and green tones. A globe that looks like an ancient map.

```html
<!DOCTYPE html>
<html lang="en">
<head>
<meta charset="utf-8">
<title>Bright Harbor International – Business Card</title>
<link href="https://fonts.googleapis.com/css2?family=PT+Sans:wght@400;700&display=swap" rel="stylesheet">
<style>
  :root {
    --page: #ffffff;
    --frame: #9a9a9a;
    --brand-blue: #1f4fa8;
    --card-gray-light: #fbfbfb;
    --card-gray-dark: #b4b4b4;
    --card-blue-top: #1a3c88;
    --card-blue-bottom: #078ed8;
    --white: #ffffff;
    --qr-line: rgba(255, 255, 255, 0.55);
    --text-font: "PT Sans", Arial, sans-serif;
  }
  html, body {
    margin: 0;
    padding: 0;
    overflow: hidden;
  }
  .canvas {
    position: relative;
    width: 1200px;
    height: 873px;
    background: var(--page);
    font-family: var(--text-font);
  }
  .sheet-frame {
    position: absolute;
    left: 0; top: 0;
    width: 1197px; height: 870px;
    border: 1px solid var(--frame);
    box-sizing: border-box;
  }
  .card {
    position: absolute;
    width: 600px;
    height: 343px;
    box-sizing: border-box;
    overflow: hidden;
  }
  .card--front {
    left: 73px; top: 84px;
    background: radial-gradient(ellipse at 50% 40%, var(--card-gray-light) 0%, #e6e6e6 40%, var(--card-gray-dark) 100%);
  }
  .card--back {
    left: 326px; top: 445px;
    background: linear-gradient(to bottom, var(--card-blue-top), var(--card-blue-bottom));
    border: 1px solid #3a5a90;
  }
  .brand {
    position: absolute;
    display: flex;
    flex-direction: column;
    align-items: center;
    color: var(--brand-blue);
    font-weight: 400;
  }
  .brand__mark {
    border-radius: 50%;
    background: currentColor;
  }
  .brand__name {
    line-height: 1;
    white-space: nowrap;
  }
  .brand__tag {
    align-self: flex-end;
    letter-spacing: 0.12em;
    line-height: 1;
    white-space: nowrap;
  }
  .card--front .brand { left: 150px; top: 82px; width: 300px; }
  .card--front .brand__mark { width: 96px; height: 96px; margin-bottom: 14px; }
  .card--front .brand__name { font-size: 46px; }
  .card--front .brand__tag { font-size: 11px; margin-top: 4px; margin-right: 8px; }

  .brand--standalone { left: 832px; top: 158px; width: 300px; }
  .brand--standalone .brand__mark { width: 96px; height: 96px; margin-bottom: 14px; }
  .brand--standalone .brand__name { font-size: 46px; }
  .brand--standalone .brand__tag { font-size: 11px; margin-top: 4px; margin-right: 4px; }

  .card--back .brand { left: 340px; top: 183px; width: 230px; color: var(--white); }
  .card--back .brand__mark { width: 70px; height: 70px; margin-bottom: 10px; }
  .card--back .brand__name { font-size: 34px; }
  .card--back .brand__tag { font-size: 9px; margin-top: 3px; margin-right: 6px; }

  .qr-space {
    position: absolute;
    right: 34px;
    top: 32px;
    width: 84px;
    height: 84px;
    border: 1px dashed var(--qr-line);
    box-sizing: border-box;
  }

  .contact {
    position: absolute;
    right: 300px;
    top: 220px;
    text-align: right;
    color: var(--white);
    white-space: nowrap;
  }
  .contact__name { font-size: 27px; line-height: 1.1; }
  .contact__title { font-size: 14px; margin-top: 4px; }
  .contact__phone { font-size: 20px; margin-top: 2px; }
  .contact__email { font-size: 13.5px; margin-top: 4px; }
</style>
</head>
<body>
<main class="canvas">
  <div class="sheet-frame"></div>

  <section class="card card--front" aria-label="Business card front">
    <div class="brand">
      <span class="brand__mark"></span>
      <span class="brand__name">Bright Harbor</span>
      <span class="brand__tag">INTERNATIONAL</span>
    </div>
  </section>

  <div class="brand brand--standalone" aria-label="Bright Harbor International logo">
    <span class="brand__mark"></span>
    <span class="brand__name">Bright Harbor</span>
    <span class="brand__tag">INTERNATIONAL</span>
  </div>

  <section class="card card--back" aria-label="Business card back">
    <div class="qr-space" role="img" aria-label="Reserved space for QR code"></div>
    <div class="contact">
      <div class="contact__name">Peter Malvo</div>
      <div class="contact__title">President</div>
      <div class="contact__phone">555-014-7392</div>
      <div class="contact__email">Email: info@brightharbor-example.com</div>
    </div>
    <div class="brand">
      <span class="brand__mark"></span>
      <span class="brand__name">Bright Harbor</span>
      <span class="brand__tag">INTERNATIONAL</span>
    </div>
  </section>
</main>
</body>
</html>
```